Slick Quillnest Ad

We've recently re-branded our business to reflect our ethos "Wealth is about more than money - it's about choice." We aim to protect your hard-earned success and help achieve your lifestyle aspirations, whether that's retiring at fifty to go globetrotting, or buying your first home. We're a financial consultancy that primarily services high-net-worth clients.

Our brand is minimalist, modern (check out our website) and the brief focuses on our strong investment return for the past 12 years.

Task: The attached brief is for a Quillnest advertisement. Please see competitor images as a guide to how 'returns' and 'branding' can both be displayed in a design.

Target Market(s)

+30

Font styles to use
Sans Serif

Requirements
Must have
• Creative should feature the strong investment return, and design aesthetic should be 'on-brand' (modern, minimalist, lifestyle focused).

```html
<!DOCTYPE html>
<html lang="en">
<head>
<meta charset="utf-8">
<title>Quillnest – Global Investment Portfolio Returns</title>
<link rel="stylesheet" href="https://fonts.googleapis.com/css2?family=Montserrat:wght@400;500;600;700&display=swap">
<style>
  :root {
    --paper: #ffffff;
    --ink: #1c1c1c;
    --olive: #a2ae2b;
    --olive-deep: #8f9a22;
    --slate: #3b4040;
    --chart-line: #4b5143;
    --rock: #a9825e;
    --snow: #eef1f2;
    --mist: #c9cfd3;
  }
  * { margin: 0; padding: 0; box-sizing: border-box; }
  html, body { width: 1200px; height: 628px; overflow: hidden; background: var(--paper); }
  .ad {
    position: relative;
    width: 1200px;
    height: 628px;
    background: var(--paper);
    font-family: "Montserrat", sans-serif;
    color: var(--ink);
  }
  .brand {
    position: absolute;
    left: 166px;
    top: 70px;
    display: flex;
    align-items: center;
    gap: 12px;
  }
  .brand-dot {
    width: 70px;
    height: 70px;
    border-radius: 50%;
    background: var(--olive);
  }
  .brand-name {
    font-size: 40px;
    font-weight: 500;
    letter-spacing: -0.5px;
    color: var(--ink);
  }
  .hero-figure {
    position: absolute;
    left: 0;
    top: 0;
    width: 1200px;
    height: 628px;
  }
  .hero-figure text {
    font-family: "Montserrat", sans-serif;
    font-weight: 700;
  }
  .headline {
    position: absolute;
    left: 410px;
    top: 404px;
    font-size: 30px;
    line-height: 42px;
    font-weight: 400;
    color: var(--ink);
    letter-spacing: -0.2px;
  }
  .headline strong { font-weight: 700; }
  .headline .highlight { color: var(--olive); font-weight: 700; }
</style>
</head>
<body>
<main class="ad">
  <div class="brand">
    <span class="brand-dot"></span>
    <span class="brand-name">Quillnest</span>
  </div>

  <svg class="hero-figure" viewBox="0 0 1200 628" aria-label="20.5 percent return with rising line chart">
    <defs>
      <linearGradient id="landscape-tone" x1="0" y1="0" x2="1" y2="1">
        <stop offset="0" stop-color="var(--rock)"/>
        <stop offset="0.35" stop-color="#c9b39a"/>
        <stop offset="0.6" stop-color="var(--snow)"/>
        <stop offset="1" stop-color="var(--mist)"/>
      </linearGradient>
      <linearGradient id="base-fade" x1="0" y1="0" x2="0" y2="1">
        <stop offset="0.55" stop-color="#fff"/>
        <stop offset="0.72" stop-color="#fff" stop-opacity="0.6"/>
        <stop offset="0.8" stop-color="#fff" stop-opacity="0"/>
      </linearGradient>
      <mask id="numeral-fade" maskUnits="userSpaceOnUse" x="0" y="0" width="1200" height="628">
        <rect x="0" y="0" width="1200" height="628" fill="url(#base-fade)"/>
      </mask>
      <linearGradient id="trend-tail" x1="0" y1="0" x2="1" y2="0">
        <stop offset="0" stop-color="var(--chart-line)"/>
        <stop offset="1" stop-color="var(--chart-line)" stop-opacity="0"/>
      </linearGradient>
    </defs>

    <g class="numerals" mask="url(#numeral-fade)">
      <text class="numeral-two" x="198" y="455" font-size="350" fill="var(--olive)" letter-spacing="-10">2</text>
      <g role="img" aria-label="Snowy mountain landscape photograph filling the numerals 0.5">
        <text class="numeral-photo" x="385" y="455" font-size="350" fill="url(#landscape-tone)" letter-spacing="-14">0.5</text>
      </g>
    </g>
    <text class="percent" x="866" y="394" font-size="190" fill="var(--slate)">%</text>

    <g class="trend">
      <polyline points="205,385 250,340 349,270 415,243 478,201 593,215 661,203 720,224 811,171"
        fill="none" stroke="var(--chart-line)" stroke-width="4" stroke-linejoin="round"/>
      <line x1="811" y1="171" x2="872" y2="146" stroke="url(#trend-tail)" stroke-width="4"/>
      <g fill="var(--paper)" stroke="var(--chart-line)" stroke-width="3.5">
        <circle cx="250" cy="340" r="7"/>
        <circle cx="349" cy="270" r="7"/>
        <circle cx="415" cy="243" r="7"/>
        <circle cx="478" cy="201" r="7"/>
        <circle cx="593" cy="215" r="7"/>
        <circle cx="661" cy="203" r="7"/>
        <circle cx="720" cy="224" r="7"/>
        <circle cx="811" cy="171" r="7"/>
      </g>
    </g>
  </svg>

  <p class="headline">
    Our <strong>Global Investment Portfolio</strong> delivered<br>
    <span class="highlight">20.5% Returns</span> over the Past 12 months.
  </p>
</main>
</body>
</html>
```